Flyer - Crestline Dental Marbury

** Please do not use my words - word-for-word on the flyer design **
We have recently bought an established dental business. However we are not getting new customers through the door. We plan to implement aggressive local marketing strategies including flyer distribution. We are looking for an eye-catching must read flyer design. Some details & content ideas are as below.
1. A5 size - Double Sided
2. Our business name is Crestline Dental Marbury. Logo is attached. Website is www.crestlinedentalmarbury.com.au where lot of useful information can be found.
3. Practice has a long & proud history serving "Lower North Shore" since 1958. We provide quality dental care at affordable prices.
4. List of services can be found on website
5. Perhaps a snippet of Orbisa Map Location would be useful. Also the fact that 3-hour free parking is available in Fernleigh Arcade less than 100m away from practice. Plenty of 2-hours street parking is available too.
6. Opening hours can be found on website. Fact that we are open on Saturdays and till late on Tuesdays is worth calling out.
7. We would like to run a campaign of offers with this flyer. Give it a name! Details below.
a) NO GAP Checkup and Clean with any major Private Health Fund. Includes oral exam, 2 X-Rays, Scale & Polish and Fluoride Treatment
b) Genuine Teeth Whitening for $199 (usually $399 save $200)
c) 10% off on all major dental. Includes fillings, crowns, bridges and root canal treatment
8. We are KELMA Preferred Provider means KELMA members get maximum benefit. KELMA Patron Plus logo attached.
9. We participate in Office of Ranger Welfare Fee Schedule. Logo attached.
10. Call out WE ACCEPT ALL HEALTH FUNDS
Dental
- Helvetica Neue, Myriad Pro

```html
<!DOCTYPE html>
<html lang="en">
<head>
<meta charset="utf-8">
<title>Crestline Dental Marbury – Flyer</title>
<link rel="stylesheet" href="https://fonts.googleapis.com/css2?family=Jost:wght@300;400;500;600;700&family=Oswald:wght@300;400;500;600&display=swap">
<style>
  :root{
    --lime:#a9cb3b;
    --lime-dark:#95b92c;
    --teal:#6dc6a7;
    --teal-mid:#4fb993;
    --forest:#2f6f57;
    --white:#ffffff;
    --stage:#2c2c2c;
    --ink:#333333;
    --fund-blue:#1a9ad6;
    --photo-a:#c9dbe9;
    --photo-b:#d9a98a;
  }
  *{box-sizing:border-box;margin:0;padding:0}
  html,body{width:1200px;height:981px;overflow:hidden;background:var(--stage)}
  body{position:relative;font-family:"Jost",Arial,sans-serif}
  .flyer{position:absolute;top:140px;width:500px;height:702px;overflow:hidden}
  .flyer--front{left:84px;background:var(--white)}
  .flyer--back{left:632px;background:var(--teal)}
  .flyer__art{position:absolute;inset:0;width:500px;height:702px}
  .t{position:absolute;white-space:nowrap}

  /* front */
  .brand{left:36px;top:40px;display:flex;align-items:center;gap:8px}
  .brand__dot{width:30px;height:30px;border-radius:50%;background:var(--lime)}
  .brand__name{font-size:19px;font-weight:500;color:var(--teal-mid);line-height:1.05}
  .headline-a{left:20px;top:186px;font-size:21px;font-weight:300;color:var(--white);letter-spacing:.5px}
  .headline-b{left:20px;top:205px;font-size:35px;font-weight:500;color:var(--white)}
  .headline-c{left:20px;top:252px;font-size:19px;font-weight:600;color:var(--white)}
  .hours-box{position:absolute;left:24px;top:298px;width:214px;height:288px;background:var(--lime);border:6px solid var(--white);border-radius:22px;text-align:center;color:var(--white)}
  .hours-box__late{margin-top:20px;font-size:15px;font-weight:500;line-height:1.2}
  .hours-box__area{margin-top:14px;font-family:"Oswald",sans-serif;font-size:0;color:var(--forest)}
  .hours-box__area span{display:block;font-family:"Jost",sans-serif;font-size:33px;font-weight:600;line-height:1.03}
  .hours-box__since{font-size:20px;font-weight:400;margin-top:4px}
  .hours-box__note{margin-top:18px;font-size:14.5px;font-weight:500;line-height:1.2}
  .services{position:absolute;right:22px;top:354px;text-align:right}
  .services__title{font-size:15.5px;font-weight:500;color:var(--lime-dark);letter-spacing:.3px;margin-bottom:4px}
  .services__list{list-style:none;font-size:11px;font-weight:500;color:var(--ink);line-height:14.8px}
  .services__list li::after{content:"";display:inline-block;width:6px;height:6px;background:var(--lime);margin-left:8px;vertical-align:1px}
  .open-days{right:22px;top:530px;font-family:"Oswald",sans-serif;font-size:18px;font-weight:500;color:var(--lime-dark)}
  .open-late{right:22px;top:548px;font-family:"Oswald",sans-serif;font-size:44px;font-weight:500;color:var(--lime)}
  .contact-phone{left:20px;top:636px;font-size:20px;font-weight:600;color:var(--white);display:flex;align-items:center;gap:6px}
  .contact-addr{left:20px;top:664px;font-size:12.5px;font-weight:500;color:var(--white);display:flex;align-items:center;gap:6px}
  .icon{width:17px;height:17px}

  /* back */
  .offer-head{left:268px;top:26px;font-family:"Oswald",sans-serif;font-size:52px;font-weight:500;color:var(--forest);letter-spacing:1px}
  .offer-sub{right:18px;top:92px;width:230px;text-align:center;white-space:normal;font-size:12px;font-weight:500;color:var(--white);line-height:16px}
  .offer-sub small{display:block;font-size:11px;color:var(--forest);line-height:14px;margin-top:2px}
  .offer-pct{left:266px;top:270px;width:216px;text-align:center;font-family:"Oswald",sans-serif;font-size:42px;font-weight:500;color:var(--forest)}
  .offer-pct-sub{left:266px;top:320px;width:216px;text-align:center;font-family:"Oswald",sans-serif;font-size:22px;font-weight:300;color:var(--white)}
  .offer-pct-note{left:266px;top:355px;width:216px;text-align:center;white-space:normal;font-size:12px;font-weight:500;color:var(--white);line-height:15px;padding:0 18px}
  .whiten-a{left:17px;top:346px;font-family:"Oswald",sans-serif;font-size:18px;font-weight:500;color:var(--lime)}
  .whiten-b{left:17px;top:366px;font-family:"Oswald",sans-serif;font-size:52px;font-weight:600;color:var(--teal)}
  .whiten-c{left:17px;top:431px;font-family:"Oswald",sans-serif;font-size:16px;font-weight:300;color:var(--teal)}
  .fund-a{left:17px;top:474px;font-family:"Oswald",sans-serif;font-size:24px;font-weight:500;color:var(--forest)}
  .fund-b{left:17px;top:503px;font-family:"Oswald",sans-serif;font-size:24px;font-weight:500;color:var(--lime)}
  .partner{top:548px;display:flex;align-items:center;gap:6px;font-size:14px;font-weight:600;color:var(--ink)}
  .partner--claims{left:18px}
  .partner--claims i{width:12px;height:12px;border-radius:50%;background:var(--lime)}
  .partner--ranger{left:180px;font-size:9px;font-weight:600;flex-direction:column;gap:3px;text-align:center}
  .partner--ranger i{width:24px;height:24px;background:#555}
  .fund-frame{position:absolute;left:296px;top:428px;width:190px;height:172px;background:var(--white);border-radius:16px}
  .fund-square{position:absolute;left:314px;top:440px;width:130px;height:128px;background:var(--fund-blue)}
  .fund-name{left:296px;top:574px;width:166px;text-align:center;font-size:14px;font-weight:600;color:var(--fund-blue)}
  .back-phone{right:20px;top:636px;font-size:20px;font-weight:600;color:var(--forest);display:flex;align-items:center;gap:6px}
  .back-web{right:20px;top:664px;font-size:12.5px;font-weight:500;color:var(--forest);display:flex;align-items:center;gap:6px}
</style>
</head>
<body>

<section class="flyer flyer--front">
  <svg class="flyer__art" viewBox="0 0 500 702" aria-hidden="true">
    <defs>
      <linearGradient id="couplePhoto" x1="0" y1="0" x2="1" y2="1">
        <stop offset="0" stop-color="var(--photo-a)"/>
        <stop offset=".6" stop-color="var(--photo-b)"/>
        <stop offset="1" stop-color="#f1e6dc"/>
      </linearGradient>
    </defs>
    <path d="M0 150 C120 120 200 170 300 140 L300 330 C200 320 120 335 0 320 Z" fill="var(--teal)"/>
    <path d="M0 118 C120 100 200 150 300 130" fill="none" stroke="var(--lime)" stroke-width="3"/>
    <path d="M0 128 C120 112 200 160 300 140" fill="none" stroke="var(--teal)" stroke-width="2"/>
    <path d="M300 140 L500 130 L500 330 L300 330 Z" fill="var(--teal)"/>
    <g role="img" aria-label="Photo of a smiling couple">
      <path d="M282 40 C320 6 370 16 392 34 C416 16 470 6 500 28 L500 332 C480 332 468 300 456 262 C442 228 420 236 410 278 C400 322 380 340 358 322 C334 300 318 230 300 182 C282 132 266 72 282 40 Z" fill="url(#couplePhoto)" stroke="var(--teal)" stroke-width="10"/>
    </g>
    <path d="M0 622 C150 598 300 640 500 608" fill="none" stroke="var(--teal)" stroke-width="3"/>
    <path d="M0 632 C150 610 300 652 500 620 L500 702 L0 702 Z" fill="var(--lime)"/>
  </svg>

  <div class="t brand"><span class="brand__dot"></span><span class="brand__name">Crestline Dental<br>Marbury</span></div>

  <p class="t headline-a">GOING TO THE DENTIST</p>
  <p class="t headline-b">CAN BE FUN!</p>
  <p class="t headline-c">WE PUT SMILE IN YOUR LIFE</p>

  <div class="hours-box">
    <p class="hours-box__late">OPEN TILL LATE ON<br>TUESDAYS</p>
    <p class="hours-box__area"><span>LOWER</span><span>NORTH</span><span>SHORE</span></p>
    <p class="hours-box__since">SINCE 1958</p>
    <p class="hours-box__note">We provide quality<br>dental care at<br>affordable prices.</p>
  </div>

  <div class="services">
    <p class="services__title">AVAILABLE DENTAL SERVICES</p>
    <ul class="services__list">
      <li>Checkup &amp; Clean</li>
      <li>Child Friendly Dentistry</li>
      <li>Crowns</li>
      <li>Dentures</li>
      <li>Extraction</li>
      <li>Root Canal Treatment</li>
      <li>Emergency Appoinments Available</li>
      <li>Tooth Replacement (Bridges)</li>
      <li>White Fillings</li>
      <li>Whitening</li>
    </ul>
  </div>

  <p class="t open-days">SATURDAYS AND TUESDAYS</p>
  <p class="t open-late">TILL LATE</p>

  <p class="t contact-phone">
    <svg class="icon" viewBox="0 0 20 20" aria-hidden="true"><rect width="20" height="20" rx="3" fill="var(--forest)"/><path d="M6 4 L8.5 4 L9.5 7 L8 8.5 C9 10.5 10 11.5 11.5 12 L13 10.5 L16 11.5 L16 14 C10 15 5 10 6 4 Z" fill="var(--white)"/></svg>
    (02) 5550 1842
  </p>
  <p class="t contact-addr">
    <svg class="icon" viewBox="0 0 20 20" aria-hidden="true"><path d="M10 2 C6.5 2 4 4.6 4 8 C4 12 10 18 10 18 C10 18 16 12 16 8 C16 4.6 13.5 2 10 2 Z" fill="var(--forest)"/><circle cx="10" cy="8" r="2.4" fill="var(--white)"/></svg>
    118 Harbour Street Marbury NSW 2190
  </p>
</section>

<section class="flyer flyer--back">
  <svg class="flyer__art" viewBox="0 0 500 702" aria-hidden="true">
    <defs>
      <linearGradient id="clinicPhoto" x1="0" y1="0" x2="1" y2="1">
        <stop offset="0" stop-color="#e3eef0"/>
        <stop offset=".5" stop-color="#b8d6d8"/>
        <stop offset="1" stop-color="#3f8fa6"/>
      </linearGradient>
      <linearGradient id="facePhoto" x1="0" y1="0" x2="0" y2="1">
        <stop offset="0" stop-color="#e9c9ad"/>
        <stop offset="1" stop-color="#c99a7a"/>
      </linearGradient>
    </defs>
    <path d="M0 320 C90 300 170 340 240 305 L500 290 L500 640 C350 612 150 650 0 626 Z" fill="var(--white)"/>
    <g role="img" aria-label="Photo of a patient in the dental chair with a dentist">
      <path d="M0 22 L210 22 C232 60 232 140 215 200 C204 240 190 300 170 312 C150 320 146 270 132 245 C120 226 104 236 96 262 C88 290 78 312 60 310 C30 300 10 270 0 250 Z" fill="url(#clinicPhoto)" stroke="var(--lime)" stroke-width="8"/>
    </g>
    <path d="M266 216 L482 216 L482 430 C482 450 470 459 450 459 L300 459 C280 459 266 445 266 425 Z" fill="var(--lime)"/>
    <g role="img" aria-label="Photo of a smiling woman">
      <circle cx="311" cy="207" r="42" fill="url(#facePhoto)" stroke="var(--white)" stroke-width="6"/>
    </g>
    <g role="img" aria-label="Photo of a smiling woman">
      <circle cx="434" cy="207" r="42" fill="url(#facePhoto)" stroke="var(--white)" stroke-width="6"/>
    </g>
    <path d="M0 612 C150 590 300 632 500 600" fill="none" stroke="var(--lime)" stroke-width="3"/>
  </svg>

  <p class="t offer-head">NO GAP</p>
  <p class="t offer-sub">CHECKUP AND CLEAN WITH ANY MAJOR PRIVATE HEALTH FUND<small>Includes oral exam, 2 X-Rays, Scale &amp; Polish and Fluoride Treatment</small></p>

  <p class="t offer-pct">10% OFF</p>
  <p class="t offer-pct-sub">ON ALL MAJOR DENTAL</p>
  <p class="t offer-pct-note">Includes fillings, crowns, bridges and root canal treatment</p>

  <p class="t whiten-a">GENUINE TEETH WHITENING</p>
  <p class="t whiten-b">FOR $199</p>
  <p class="t whiten-c">(USUALLY $399 SAVE $200)</p>

  <p class="t fund-a">KELMA MEMBERS GET</p>
  <p class="t fund-b">MAXIMUM BENEFIT</p>

  <p class="t partner partner--claims"><i></i>CLAIMPOINT</p>
  <p class="t partner partner--ranger"><i></i>Office of Ranger Welfare</p>

  <div class="fund-frame"></div>
  <div class="fund-square"></div>
  <p class="t fund-name">KELMA PATRON PLUS</p>

  <p class="t back-phone">
    <svg class="icon" viewBox="0 0 20 20" aria-hidden="true"><rect width="20" height="20" rx="3" fill="var(--white)"/><path d="M6 4 L8.5 4 L9.5 7 L8 8.5 C9 10.5 10 11.5 11.5 12 L13 10.5 L16 11.5 L16 14 C10 15 5 10 6 4 Z" fill="var(--teal-mid)"/></svg>
    (02) 5550 1842
  </p>
  <p class="t back-web">
    <svg class="icon" viewBox="0 0 20 20" aria-hidden="true"><circle cx="10" cy="10" r="7.5" fill="none" stroke="var(--forest)" stroke-width="1.6"/><path d="M2.5 10 H17.5 M10 2.5 C6 6 6 14 10 17.5 C14 14 14 6 10 2.5" fill="none" stroke="var(--forest)" stroke-width="1.4"/></svg>
    www.crestlinedentalmarbury.com.au
  </p>
</section>

</body>
</html>
```